Marwick Agency (http://mk.fennoweb-studio.com/)

We are looking for a similar design to what we have, but more professional looking and cleaned up with links and logo that is not so grainy looking. We are an independent insurance agency marketing to personal and commercial clients. We offer all commercial lines markets and all personal lines. We target excavators, landscapers, restaurants, golf courses, contractors. Please look at http://mk.fennoweb-studio.com/ which we had designed but do not like it, it will give you an idea of what we are looking for.

Target Market(s)

Commercial and personal insurance. All business products and all personal (homeowners, auto, antique auto, umbrella)

Industry/Entity Type

It Professional

Logo Text

Knowledge Building Your Assurance

Number of Pages Required

5+ page

Colors
000000
848484
0255a3

```html
<!DOCTYPE html>
<html lang="en">
<head>
<meta charset="utf-8">
<title>Marwick Agency</title>
<link href="https://fonts.googleapis.com/css2?family=Noto+Serif&family=Open+Sans:ital,wght@0,400;0,600;0,700;1,400;1,600&family=Roboto:wght@400;500&display=swap" rel="stylesheet">
<style>
:root{
  --blue:#0255a3;
  --ink:#000000;
  --grey:#848484;
  --text:#3a3a3a;
  --band:#f6f6f6;
  --line:#dcdcdc;
  --orange:#f7941d;
  --quote-btn:#d9dfe2;
  --footer-bar:#111111;
  --white:#ffffff;
}
*{box-sizing:border-box;margin:0;padding:0}
html,body{width:762px;height:1200px;overflow:hidden;background:var(--white)}
body{font-family:"Open Sans",Arial,sans-serif;color:var(--text);position:relative}
/* header */
.site-header{position:absolute;left:0;top:0;width:762px;height:58px;border-top:2px solid var(--blue);background:var(--white)}
.brand{position:absolute;left:106px;top:20px;display:flex;align-items:center;gap:7px}
.brand-dot{width:32px;height:20px;border-radius:50%;background:var(--blue)}
.brand-name{font-family:"Noto Serif",Georgia,serif;font-size:19px;color:var(--blue);line-height:1}
.header-call{position:absolute;left:550px;top:17px;display:flex;gap:5px}
.header-call svg{margin-top:3px}
.header-call small{display:block;font-size:8px;color:var(--grey)}
.header-call strong{display:block;font-size:11.5px;color:var(--blue);font-weight:700;margin-top:-1px}
.main-nav{position:absolute;left:0;top:58px;width:762px;height:22px;background:var(--blue)}
.main-nav a{position:absolute;top:6px;font-size:8px;font-weight:600;color:var(--white);text-decoration:none;letter-spacing:.1px}
/* hero */
.hero{position:absolute;left:0;top:80px;width:762px;height:248px;overflow:hidden}
.hero-photo{position:absolute;inset:0;background:linear-gradient(90deg,#b9c3cc 0%,#c9b4a6 22%,#6a6a70 40%,#e6e4df 55%,#f1efea 100%)}
.hero-title{position:absolute;left:409px;top:47px;font-family:"Roboto",Arial,sans-serif;font-weight:400;font-size:20px;line-height:25px;color:#1b1b1b;letter-spacing:.3px}
.hero-btn{position:absolute;left:413px;top:145px;width:109px;height:19px;background:var(--orange);color:#2a1600;font-size:8px;font-weight:700;display:flex;align-items:center;justify-content:center}
.hero-arrow{position:absolute;top:111px;width:27px;height:27px;background:rgba(120,120,120,.75);display:flex;align-items:center;justify-content:center}
/* intro */
.section-title{font-family:"Noto Serif",Georgia,serif;color:var(--blue);font-size:17px;text-align:center;position:absolute;left:0;width:762px;font-weight:400}
.intro-text{position:absolute;left:128px;top:381px;width:506px;font-size:7.3px;line-height:11.6px;text-align:center;color:#333}
.intro-text b{font-weight:700;color:#111}
/* services */
.services{position:absolute;left:0;top:478px;width:762px;height:328px;background:var(--band);border-bottom:1px solid var(--line)}
.services-sub{position:absolute;left:0;width:762px;top:54px;font-size:7.5px;text-align:center;color:#333}
.service-card{position:absolute;top:81px;width:133px;height:219px;background:var(--white);border:1px solid var(--line)}
.service-card h3{height:30px;background:var(--blue);color:var(--white);font-size:11px;font-weight:600;text-align:center;line-height:30px;margin:-1px -1px 0}
.service-photo{height:95px}
.service-card p{font-size:7px;line-height:10.4px;text-align:center;padding:5px 3px 0;color:#444;letter-spacing:-.05px}
.quote-btn{position:absolute;left:-1px;right:-1px;bottom:-1px;height:22px;background:var(--quote-btn);display:flex;align-items:center;justify-content:center;gap:5px;font-size:9.2px;font-weight:600;color:#222}
/* testimonials */
.testimonial{position:absolute;top:867px;width:176px;height:73px;border:1px solid var(--line);border-radius:3px;background:var(--white);padding:8px 9px}
.testimonial p{font-size:6.8px;line-height:10.4px;font-style:italic;font-weight:400;color:#222;white-space:nowrap}
.testimonial::after{content:"";position:absolute;left:20px;bottom:-6px;width:10px;height:10px;background:var(--white);border-right:1px solid var(--line);border-bottom:1px solid var(--line);transform:rotate(45deg)}
.testimonial-name{position:absolute;top:948px;font-size:7.5px;font-style:italic;font-weight:600;color:#222}
/* footer */
.site-footer{position:absolute;left:0;top:990px;width:762px;height:180px;background:var(--blue);color:var(--white)}
.footer-tag{position:absolute;left:100px;top:15px;font-family:"Noto Serif",Georgia,serif;font-size:14px}
.footer-call{position:absolute;left:509px;top:17px;display:flex;align-items:center;gap:6px;font-size:8.5px}
.footer-call strong{font-size:10px}
.footer-rule{position:absolute;left:100px;top:37px;width:562px;height:1px;background:rgba(255,255,255,.25)}
.footer-col{position:absolute;top:54px}
.footer-col h4{font-size:8.5px;font-weight:600;margin-bottom:8px}
.footer-col li{list-style:none;font-size:7.2px;line-height:12px}
.footer-col li::before{content:"» ";}
.social{position:absolute;top:52px;width:15px;height:15px;border-radius:2px;background:var(--white)}
.badge{position:absolute;left:338px;top:76px;width:118px;height:73px;border-radius:36px;background:var(--white);border:3px solid #c8d6e6}
.contact-list{font-size:7px;line-height:11.5px}
.contact-list .office{font-weight:700;font-size:6.8px;margin-bottom:2px}
.contact-list div{display:flex;gap:4px;align-items:flex-start}
.contact-list svg{flex:none;margin-top:2px}
.footer-bar{position:absolute;left:0;top:1170px;width:762px;height:30px;background:var(--footer-bar);color:#bbb;font-size:6.5px;text-align:center;line-height:30px}
</style>
</head>
<body>

<header class="site-header">
  <div class="brand"><span class="brand-dot"></span><span class="brand-name">Marwick Agency</span></div>
  <div class="header-call">
    <svg width="18" height="18" viewBox="0 0 18 18"><circle cx="9" cy="9" r="8" fill="none" stroke="#9a9a9a" stroke-width="1.2"/><path d="M6 5l2 2-1 1c.6 1.3 1.5 2.2 2.8 2.8l1-1 2 2-1.3 1.3C8.5 12.8 5.2 9.5 4.7 6.3z" fill="#9a9a9a"/></svg>
    <div><small>Call us today:</small><strong>1-888-555-0142</strong></div>
  </div>
</header>

<nav class="main-nav">
  <a style="left:116px">HOME</a>
  <a style="left:178px">ABOUT US</a>
  <a style="left:256px">PERSONAL INSURANCE</a>
  <a style="left:380px">BUSINESS INSURANCE</a>
  <a style="left:500px">SERVICE CENTER</a>
  <a style="left:600px">CONTACT US</a>
</nav>

<section class="hero">
  <div class="hero-photo" role="img" aria-label="Insurance advisor reviewing a policy document with a senior couple in a bright living room"></div>
  <h1 class="hero-title">SMALL ENOUGH TO CARE,<br>BIG ENOUGH TO MAKE A<br>DIFFERENCE</h1>
  <div class="hero-btn">LEARN ABOUT MORE...</div>
  <div class="hero-arrow" style="left:29px"><svg width="10" height="12" viewBox="0 0 10 12"><path d="M8 1L2 6l6 5" fill="none" stroke="#fff" stroke-width="2.5"/></svg></div>
  <div class="hero-arrow" style="left:710px"><svg width="10" height="12" viewBox="0 0 10 12"><path d="M2 1l6 5-6 5" fill="none" stroke="#fff" stroke-width="2.5"/></svg></div>
</section>

<h2 class="section-title" style="top:352px">Marwick Agency are an Independent Agency</h2>
<p class="intro-text"><b>We are an Independent Agency , which allows us to keep your needs in mind.</b><br>
Established in 1950 by the Hale family, the Marwick Agency was founded on the philosophy of offering personal, professional service. Since then we have grown into a full service agency with a staff of 10 insurance specialist serving over 2,000 individuals and 800 businesses.<br>
We do not work for an insurance company we work for you. we work on your side when you have a loss and follow through to see that you get affair, prompt, payment. We represent a carefully selected group of reputable insurance companies, and we place your policy with the company offering the best coverage at the best possible price. Please explore our website and let us know how we can help serve your insurance needs.</p>

<section class="services">
  <h2 class="section-title" style="top:24px">Our Services</h2>
  <p class="services-sub">Please find information about our agency, its principles , and the various types of insurance coverages that we provide.</p>

  <article class="service-card" style="left:100px">
    <h3>BUSINESS INSURANCE</h3>
    <div class="service-photo" role="img" aria-label="Business clients shaking hands with an advisor" style="background:linear-gradient(90deg,#e8e2d8,#b8a89a 45%,#3a3d44)"></div>
    <p>Lorem ipsum dolor sit amet, consec adipiscing elit, sed do eiusmod temp incididunt ut labore et dolore magna aliqua. Ut enim ad minim venim, quis nostrud exercitation ullamco laboris.</p>
    <div class="quote-btn"><svg width="10" height="10" viewBox="0 0 10 10"><rect x="1" y="2" width="7" height="7" fill="none" stroke="#222"/><path d="M4 6l5-5" stroke="#222" stroke-width="1.3"/></svg>GET A FREE QUOTE</div>
  </article>

  <article class="service-card" style="left:243px">
    <h3>AUTO INSURANCE</h3>
    <div class="service-photo" role="img" aria-label="Hands sheltering a small red toy car" style="background:linear-gradient(180deg,#6f8fb8,#9db3cf 55%,#d7a28e)"></div>
    <p>Lorem ipsum dolor sit amet, consec adipiscing elit, sed do eiusmod temp incididunt ut labore et dolore magna aliqua. Ut enim ad minim venim, quis nostrud exercitation ullamco laboris.</p>
    <div class="quote-btn"><svg width="10" height="10" viewBox="0 0 10 10"><rect x="1" y="2" width="7" height="7" fill="none" stroke="#222"/><path d="M4 6l5-5" stroke="#222" stroke-width="1.3"/></svg>GET A FREE QUOTE</div>
  </article>

  <article class="service-card" style="left:386px">
    <h3>LIFE INSURANCE</h3>
    <div class="service-photo" role="img" aria-label="Black and white close-up of a baby's hand held in an adult's hand" style="background:radial-gradient(circle at 50% 50%,#d8d8d8,#6a6a6a 45%,#111 80%)"></div>
    <p>Lorem ipsum dolor sit amet, consec adipiscing elit, sed do eiusmod temp incididunt ut labore et dolore magna aliqua. Ut enim ad minim venim, quis nostrud exercitation ullamco laboris.</p>
    <div class="quote-btn"><svg width="10" height="10" viewBox="0 0 10 10"><rect x="1" y="2" width="7" height="7" fill="none" stroke="#222"/><path d="M4 6l5-5" stroke="#222" stroke-width="1.3"/></svg>GET A FREE QUOTE</div>
  </article>

  <article class="service-card" style="left:529px">
    <h3>HOME INSURANCE</h3>
    <div class="service-photo" role="img" aria-label="Hands protecting a small model house against a blue sky" style="background:linear-gradient(180deg,#3f78c0,#8fb4e0 60%,#e9c6b4)"></div>
    <p>Lorem ipsum dolor sit amet, consec adipiscing elit, sed do eiusmod temp incididunt ut labore et dolore magna aliqua. Ut enim ad minim venim, quis nostrud exercitation ullamco laboris.</p>
    <div class="quote-btn"><svg width="10" height="10" viewBox="0 0 10 10"><rect x="1" y="2" width="7" height="7" fill="none" stroke="#222"/><path d="M4 6l5-5" stroke="#222" stroke-width="1.3"/></svg>GET A FREE QUOTE</div>
  </article>
</section>

<h2 class="section-title" style="top:831px">What Our Customers Say</h2>
<blockquote class="testimonial" style="left:100px"><p>" Lorem Ipsum is simply dummy text of the<br>printing and typesetting industry. Lorem Ipsum<br>has been the industry's standard dummy text<br>ever since the 1500s, when an unknown printer<br>took a galley of type and scrambled."</p></blockquote>
<blockquote class="testimonial" style="left:293px"><p>" Lorem Ipsum is simply dummy text of the<br>printing and typesetting industry. Lorem Ipsum<br>has been the industry's standard dummy text<br>ever since the 1500s, when an unknown printer<br>took a galley of type and scrambled."</p></blockquote>
<blockquote class="testimonial" style="left:486px"><p>" Lorem Ipsum is simply dummy text of the<br>printing and typesetting industry. Lorem Ipsum<br>has been the industry's standard dummy text<br>ever since the 1500s, when an unknown printer<br>took a galley of type and scrambled."</p></blockquote>
<span class="testimonial-name" style="left:120px">Lorem Ipsum</span>
<span class="testimonial-name" style="left:313px">Lorem Ipsum</span>
<span class="testimonial-name" style="left:506px">Lorem Ipsum</span>

<footer class="site-footer">
  <p class="footer-tag">We are Trusted Professionals on Your Side</p>
  <div class="footer-call">
    <svg width="14" height="14" viewBox="0 0 14 14"><circle cx="7" cy="7" r="7" fill="#fff"/><path d="M4.5 3.5l1.5 1.5-.8.8c.5 1 1.2 1.7 2.2 2.2l.8-.8 1.5 1.5-1 1C6.4 9.3 4.6 7.6 3.5 4.5z" fill="#0255a3"/></svg>
    <span>Call Us Today!</span><strong>1-888-555-0142</strong>
  </div>
  <div class="footer-rule"></div>

  <div class="footer-col" style="left:100px">
    <h4>Quick Links</h4>
    <ul><li>Home</li><li>Personal Insurance</li><li>Business Insurance</li><li>Service Center</li><li>About Us</li><li>Contact Us</li></ul>
  </div>
  <div class="footer-col" style="left:212px">
    <h4>Services</h4>
    <ul><li>Carpenters</li><li>Electricians</li><li>Excavators</li><li>Golf Courses</li><li>Landscapers</li><li>Plumbing</li></ul>
  </div>

  <span class="social" style="left:369px"></span>
  <span class="social" style="left:389px"></span>
  <span class="social" style="left:409px"></span>
  <div class="badge"></div>

  <div class="footer-col contact-list" style="left:497px">
    <h4>Contact Us</h4>
    <p class="office">ASHBROOK OFFICE:</p>
    <div><svg width="6" height="8" viewBox="0 0 6 8"><path d="M3 0a3 3 0 0 1 3 3c0 2-3 5-3 5S0 5 0 3a3 3 0 0 1 3-3z" fill="#fff"/></svg><span>Marwick Agency, 48 Orchard Lane, Suite C<br>Ashbrook, NJ 07990</span></div>
    <div><svg width="7" height="7" viewBox="0 0 7 7"><path d="M1 0l2 2-1 1c.4.8.9 1.3 1.7 1.7l1-1 2 2L5.6 7C3 6.6.4 4 0 1.4z" fill="#fff"/></svg><span>Phone: 908-555-0120</span></div>
    <div><svg width="7" height="7" viewBox="0 0 7 7"><rect x="0" y="2" width="7" height="5" fill="#fff"/><rect x="1.5" y="0" width="4" height="2.5" fill="#fff"/></svg><span>Fax: 908-555-0199</span></div>
    <div><svg width="8" height="6" viewBox="0 0 8 6"><rect width="8" height="6" fill="#fff"/><path d="M0 0l4 3 4-3" fill="none" stroke="#0255a3"/></svg><span>admin@marwickagency.com</span></div>
  </div>
</footer>

<div class="footer-bar">Copyright © 2015 Marwick Agency. All Rights Reserved.</div>

</body>
</html>
```